Need new Spot UV Business Card design

We are looking for a new business card design incorporating Spot UV in black & white options / versions. See examples files and Tobin Ashgrove Design logo.
You can see our website at www.tobinashgrove.ca. We want something classy but yet modern. We are open to black or black and/or white on white with the spot uv. We are open to portrait or landscape. Size should be standard 3.5" x 2". The front of the card should focus on the logo and name "Tobin Ashgrove" only. Fonts used should be "Open sans" or "PT Sans".

Target Market(s)

Mid to high end

Industry/Entity Type

Business

Contact Information for Business Card

Tobin Velasko
416.382.4417
tobin@tobinashgrove.ca
www.tobinashgrove.ca
4175 Brightwell Blvd. E Suite 308
Mississauga, ON L5T 2K9

Requirements
Must have
• Name & Logo

```html
<!DOCTYPE html>
<html lang="en">
<head>
<meta charset="utf-8">
<title>Tobin Ashgrove Design — Spot UV Business Card</title>
<link rel="stylesheet" href="https://fonts.googleapis.com/css2?family=Open+Sans:wght@400;600;700&display=swap">
<style>
  :root {
    --stage: #3b322d;
    --card: #1c1c1d;
    --gloss: #2a2a2c;
    --gloss-hi: #5a5858;
    --ink: #e9e9e9;
    --ink-soft: #c9c9c9;
  }
  html, body {
    margin: 0;
    width: 1200px;
    height: 716px;
    overflow: hidden;
    background: var(--stage);
    font-family: "Open Sans", sans-serif;
  }
  .stage {
    position: relative;
    width: 1200px;
    height: 716px;
  }
  .card {
    position: absolute;
    top: 215px;
    width: 500px;
    height: 286px;
    background: var(--card);
    border-radius: 4px;
    box-shadow: 0 10px 24px rgba(0,0,0,0.45);
    overflow: hidden;
  }
  .card--front { left: 70px; }
  .card--back  { left: 630px; }

  /* Front: brand in spot UV */
  .front-brand {
    position: absolute;
    inset: 0;
    display: flex;
    align-items: center;
    justify-content: center;
    gap: 14px;
  }
  .front-brand__square {
    width: 30px;
    height: 30px;
    border: 3px solid var(--gloss-hi);
    box-sizing: border-box;
  }
  .front-brand__name {
    font-size: 24px;
    font-weight: 600;
    letter-spacing: 2px;
    color: var(--gloss-hi);
    text-transform: uppercase;
  }

  /* Back: contact side */
  .back-brand {
    position: absolute;
    left: 28px;
    top: 26px;
    display: flex;
    align-items: center;
    gap: 10px;
  }
  .back-brand__square {
    width: 34px;
    height: 34px;
    border: 2px solid var(--ink);
    box-sizing: border-box;
  }
  .back-brand__name {
    font-size: 19px;
    font-weight: 400;
    line-height: 1.05;
    letter-spacing: 1px;
    color: var(--ink);
    text-transform: uppercase;
  }
  .uv-block {
    position: absolute;
    right: 30px;
    top: 62px;
    width: 150px;
    height: 190px;
    background: linear-gradient(135deg, var(--gloss) 0%, #3c3b3c 45%, var(--gloss) 100%);
    border-radius: 2px;
  }
  .contact {
    position: absolute;
    left: 28px;
    top: 120px;
    width: 270px;
    color: var(--ink-soft);
    font-size: 11.5px;
    line-height: 1.7;
  }
  .contact__name {
    font-size: 16px;
    font-weight: 700;
    color: var(--ink);
    margin: 0 0 8px;
  }
  .contact__row {
    display: flex;
    align-items: center;
    gap: 9px;
  }
  .contact__icon {
    width: 11px;
    height: 11px;
    fill: var(--ink-soft);
    flex: none;
  }
  .contact__address {
    margin-top: 2px;
    line-height: 1.5;
  }
</style>
</head>
<body>
<main class="stage">

  <section class="card card--front" aria-label="Business card front">
    <div class="front-brand">
      <span class="front-brand__square"></span>
      <span class="front-brand__name">Tobin Ashgrove</span>
    </div>
  </section>

  <section class="card card--back" aria-label="Business card back">
    <div class="back-brand">
      <span class="back-brand__square"></span>
      <span class="back-brand__name">Tobin<br>Ashgrove</span>
    </div>

    <div class="uv-block"></div>

    <div class="contact">
      <p class="contact__name">Tobin Velasko</p>
      <div class="contact__row">
        <svg class="contact__icon" viewBox="0 0 24 24" aria-hidden="true"><path d="M6.6 10.8a15.1 15.1 0 0 0 6.6 6.6l2.2-2.2a1 1 0 0 1 1-.25 11.4 11.4 0 0 0 3.6.57 1 1 0 0 1 1 1V20a1 1 0 0 1-1 1A17 17 0 0 1 3 4a1 1 0 0 1 1-1h3.5a1 1 0 0 1 1 1c0 1.25.2 2.45.57 3.57a1 1 0 0 1-.25 1z"/></svg>
        <span>416.382.4417</span>
      </div>
      <div class="contact__row">
        <svg class="contact__icon" viewBox="0 0 24 24" aria-hidden="true"><path d="M2 5h20v14H2z M4 7v.5l8 5 8-5V7z" fill-rule="evenodd"/></svg>
        <span>tobin@tobinashgrove.ca</span>
      </div>
      <div class="contact__row">
        <svg class="contact__icon" viewBox="0 0 24 24" aria-hidden="true"><path d="M12 2a10 10 0 1 0 0 20 10 10 0 0 0 0-20zm6.9 6h-2.9a15.6 15.6 0 0 0-1.4-3.6A8 8 0 0 1 18.9 8zM12 4a14 14 0 0 1 1.9 4h-3.8A14 14 0 0 1 12 4zM4.3 14a8 8 0 0 1 0-4h3.4a16 16 0 0 0 0 4zm.8 2h2.9a15.6 15.6 0 0 0 1.4 3.6A8 8 0 0 1 5.1 16zM8 8H5.1a8 8 0 0 1 4.3-3.6A15.6 15.6 0 0 0 8 8zm4 12a14 14 0 0 1-1.9-4h3.8A14 14 0 0 1 12 20zm2.3-6H9.7a14.7 14.7 0 0 1 0-4h4.6a14.7 14.7 0 0 1 0 4zm.3 5.6a15.6 15.6 0 0 0 1.4-3.6h2.9a8 8 0 0 1-4.3 3.6zm1.7-5.6a16 16 0 0 0 0-4h3.4a8 8 0 0 1 0 4z"/></svg>
        <span>www.tobinashgrove.ca</span>
      </div>
      <div class="contact__address">4175 Brightwell Blvd. E Suite 308<br>Mississauga, ON L5T 2K9</div>
    </div>
  </section>

</main>
</body>
</html>
```